Design concept Visual UI of future mobile app - healthcare

Hi,
I'm looking for a top designer, innovative with strong experience in user interface

The app will be connected to a future health website related to depression and addiction by helping the user to track the moods, tired, anxiety using this mobile app.

I attached the deck of the overall project but I can send you a specific presentation for the app only

thanks

Target Market(s)

Switzerland, UK, Germany and France

Industry/Entity Type

Mental Health

Logo Text

Health, hope

Font styles to use
Sans Serif

Colors
cee9f5
33a6d7
0692cd
0255a3
3276b5
85abd2

Requirements
Must have
• keep it simple, easy to navigate
• The user should be able to track the moods on a daily basis,
• sleep time, and rate how the feel on the day
• To be able to get information from the tally box of bront
Nice to have
• to be able share this app with a friend

```html
<!DOCTYPE html>
<html lang="en">
<head>
<meta charset="utf-8">
<title>Calm Pulse – Home Screen</title>
<link href="https://fonts.googleapis.com/css2?family=Roboto:wght@300;400&display=swap" rel="stylesheet">
<style>
  :root {
    --page-bg: #e9e6e1;
    --sky-top: #3a8fd6;
    --sky-mid: #5cb0e6;
    --sky-low: #8ccbef;
    --sky-haze: #cee9f5;
    --text-light: #ffffff;
    --menu-fill: rgba(133, 171, 210, 0.55);
    --message-fill: #3276b5;
    --mark-fill: #0255a3;
  }
  * { margin: 0; padding: 0; box-sizing: border-box; }
  html, body {
    width: 1200px;
    height: 800px;
    overflow: hidden;
    background: var(--page-bg);
    font-family: "Roboto", sans-serif;
  }
  .canvas {
    position: relative;
    width: 1200px;
    height: 800px;
  }
  .app-screen {
    position: absolute;
    left: 400px;
    top: 44px;
    width: 400px;
    height: 712px;
    overflow: hidden;
    color: var(--text-light);
  }
  .sky-backdrop {
    position: absolute;
    inset: 0;
    background:
      radial-gradient(ellipse 70% 30% at 50% 45%, rgba(206, 233, 245, 0.55), transparent 70%),
      radial-gradient(ellipse 60% 18% at 75% 72%, rgba(255, 255, 255, 0.45), transparent 70%),
      radial-gradient(ellipse 50% 14% at 20% 92%, rgba(255, 255, 255, 0.35), transparent 70%),
      linear-gradient(180deg, var(--sky-top) 0%, var(--sky-mid) 35%, var(--sky-low) 75%, var(--sky-haze) 100%);
  }
  .status-bar {
    position: absolute;
    top: 0; left: 0; right: 0;
    height: 22px;
    display: flex;
    align-items: center;
    justify-content: space-between;
    padding: 0 8px;
    font-size: 11px;
    font-weight: 400;
    background: rgba(0, 0, 0, 0.18);
  }
  .status-carrier, .status-battery { display: flex; align-items: center; gap: 4px; }
  .signal-dots { letter-spacing: -1px; font-size: 10px; }
  .nav-bar {
    position: absolute;
    top: 36px; left: 16px; right: 16px;
    display: flex;
    justify-content: space-between;
    align-items: center;
  }
  .brand {
    position: absolute;
    top: 78px; left: 0; right: 0;
    display: flex;
    flex-direction: column;
    align-items: center;
    gap: 14px;
  }
  .brand-dot {
    width: 44px; height: 44px;
    border-radius: 50%;
    background: var(--mark-fill);
  }
  .brand-name {
    font-size: 22px;
    font-weight: 300;
    letter-spacing: 0.5px;
  }
  .main-menu {
    position: absolute;
    top: 190px; left: 0; right: 0;
    display: flex;
    flex-direction: column;
    align-items: center;
    gap: 10px;
    list-style: none;
  }
  .menu-item {
    background: var(--menu-fill);
    padding: 6px 18px;
    font-size: 18px;
    font-weight: 300;
  }
  .mood-note {
    position: absolute;
    top: 372px; left: 70px; right: 70px;
    text-align: center;
    font-size: 14px;
    font-weight: 300;
    line-height: 1.35;
  }
  .message-badge {
    position: absolute;
    top: 462px; left: 50%;
    transform: translateX(-50%);
    background: var(--message-fill);
    padding: 7px 14px;
    font-size: 18px;
    font-weight: 400;
    white-space: nowrap;
  }
</style>
</head>
<body>
<div class="canvas">
  <main class="app-screen">
    <div class="sky-backdrop" role="img" aria-label="Soft blue sky with light clouds"></div>

    <div class="status-bar">
      <span class="status-carrier"><span class="signal-dots">●●●○○</span> NORA
        <svg width="12" height="9" viewBox="0 0 12 9" aria-hidden="true"><path d="M1 3.5a7 7 0 0 1 10 0M3 5.5a4 4 0 0 1 6 0" stroke="#fff" stroke-width="1.2" fill="none"/><circle cx="6" cy="7.6" r="1" fill="#fff"/></svg>
      </span>
      <span class="status-time">4:21 PM</span>
      <span class="status-battery">100%
        <svg width="22" height="10" viewBox="0 0 22 10" aria-hidden="true"><rect x="0.5" y="0.5" width="18" height="9" rx="2" stroke="#fff" fill="none"/><rect x="2" y="2" width="15" height="6" rx="1" fill="#fff"/><rect x="19.5" y="3" width="1.8" height="4" fill="#fff"/></svg>
      </span>
    </div>

    <nav class="nav-bar">
      <svg class="menu-icon" width="20" height="16" viewBox="0 0 20 16" aria-label="Menu"><path d="M1 2h18M1 8h18M1 14h18" stroke="#fff" stroke-width="2"/></svg>
      <svg class="next-icon" width="12" height="18" viewBox="0 0 12 18" aria-label="Next"><path d="M2 2l8 7-8 7" stroke="#fff" stroke-width="1.5" fill="none"/></svg>
    </nav>

    <header class="brand">
      <span class="brand-dot"></span>
      <h1 class="brand-name">CALM PULSE</h1>
    </header>

    <ul class="main-menu">
      <li class="menu-item">Whats New Today?</li>
      <li class="menu-item">Tracking Graphs</li>
      <li class="menu-item">Personal Information</li>
    </ul>

    <p class="mood-note">According to our studies Calm Pulse App has potential to improve your mood by 16%</p>

    <div class="message-badge">You have 03 messages</div>
  </main>
</div>
</body>
</html>
```